Keel Harbor Windows & Doors

We are an aluminum windows & doors manufacturer. Need a professional & vision appealing web design. It should reflects our professional business character, but with very user-friendly interface( catch eyes, use simple icon or symbol to make it easy to read...) Don't copy : ) but can use some competitor's web (https://www.brimfordglazing.example) (www.qelmoframes.example) to have a glance on our target and web content as reference

Target Market(s)

Homeowner and Professional (Builder / Developer/ Architect & window installer)

Industry/Entity Type

Manufacturer

Font styles to use
Serif
Sans Serif

Requirements
Must have
• Have 3 serials products. Residential (value for money) Commercial (Professional and quality) Architectural (Bold & funky)
• Color match or harmony with the selected logo design
Nice to have
• Project gallery display, have online free quote to upload files, can insert video or cartoon
Should not have
• no limitation on your imagination ; )

```html
<!DOCTYPE html>
<html lang="en">
<head>
<meta charset="utf-8">
<title>Keel Harbor Windows &amp; Doors</title>
<link href="https://fonts.googleapis.com/css2?family=Lato:wght@300;400;700;900&family=Oswald:wght@400;500&display=swap" rel="stylesheet">
<style>
:root{
  --green:#7dc243;
  --green-dark:#68a934;
  --ink:#222222;
  --dark:#232323;
  --dark-2:#2b2b2b;
  --grey-text:#666666;
  --light-grey:#efefef;
  --white:#ffffff;
  --line:#dcdcdc;
}
*{box-sizing:border-box;margin:0;padding:0}
html,body{width:1200px;height:3422px;overflow:hidden}
body{position:relative;font-family:"Lato",Arial,sans-serif;color:var(--ink);background:var(--white)}
.abs{position:absolute}
.photo{position:absolute;display:block}

/* Header */
.site-header{position:absolute;left:0;top:0;width:1200px;height:103px;background:var(--white)}
.brand{position:absolute;left:130px;top:22px;display:flex;align-items:center;gap:10px}
.brand-mark{width:26px;height:26px;background:var(--green)}
.brand-name{font-size:22px;font-weight:700;color:var(--green);letter-spacing:.5px}
.main-nav{position:absolute;left:308px;top:38px;display:flex;gap:28px;font-size:13px;color:#555}
.main-nav a{color:inherit;text-decoration:none;padding-bottom:8px}
.main-nav .active{color:var(--green);border-bottom:2px solid var(--green)}
.header-phone{position:absolute;left:798px;top:33px;width:138px;height:36px;border-top:1px solid var(--green);border-bottom:1px solid var(--green);display:flex;align-items:center;justify-content:center;gap:6px;font-family:"Oswald",sans-serif;font-size:17px}
.btn{display:inline-flex;align-items:center;justify-content:center;text-decoration:none;font-size:13px}
.btn-green{background:var(--green);color:var(--white)}
.header-quote{position:absolute;left:964px;top:36px;width:104px;height:32px}

/* Hero */
.hero{position:absolute;left:0;top:103px;width:1200px;height:399px;overflow:hidden}
.hero-photo{left:0;top:0;width:1200px;height:399px;background:linear-gradient(90deg,#c7b9a3 0%,#e9e4dc 22%,#a98967 48%,#6f6457 70%,#d6d0c7 100%)}
.hero-arrow{position:absolute;top:182px;width:22px;height:32px;display:flex;align-items:center;justify-content:center}
.hero-arrow.prev{left:100px;background:rgba(0,0,0,.6)}
.hero-arrow.next{left:1072px;background:var(--green)}
.hero-badge{position:absolute;left:474px;top:68px;width:252px;height:252px;border-radius:50%;background:var(--white);overflow:hidden}
.hero-badge-top{position:absolute;left:0;top:0;width:252px;height:108px;background:var(--dark);color:var(--white);text-align:center;padding-top:48px;font-size:22px}
.hero-badge-bottom{position:absolute;left:0;bottom:0;width:252px;height:78px;background:#3a78c9;color:var(--white);font-size:14px;font-style:italic;text-align:center;padding-top:18px}
.hero-ribbon{position:absolute;left:433px;top:152px;width:324px;height:83px;background:var(--green);color:var(--white);text-align:center;padding-top:16px}
.hero-ribbon .line1{font-size:17px;font-weight:700}
.hero-ribbon .line2{font-size:14px;margin-top:8px;letter-spacing:.5px}

/* Support bar */
.support-bar{position:absolute;left:0;top:502px;width:1200px;height:96px;background:var(--dark);color:var(--white)}
.support-text{position:absolute;left:200px;top:30px}
.support-text h3{font-size:19px;font-weight:400}
.support-text p{font-size:11px;margin-top:3px;color:#ddd}
.support-icon{position:absolute;left:155px;top:28px}
.support-chev{position:absolute;left:664px;top:36px}
.support-contact{position:absolute;left:731px;top:27px;width:130px;height:42px}
.support-free{position:absolute;left:877px;top:27px;width:168px;height:42px;border:1px solid var(--green);color:var(--white)}

/* Section titles */
.section-title{position:absolute;left:0;width:1200px;text-align:center;font-size:25px;font-weight:700}
.section-title em{font-style:normal;color:var(--green)}
.section-title::after{content:"";display:block;width:54px;height:2px;background:var(--line);margin:12px auto 0}

/* Services */
.service-card{position:absolute;top:732px;width:280px;height:320px;overflow:hidden}
.service-card .photo{left:0;top:0;width:100%;height:100%}
.service-label{position:absolute;left:0;bottom:0;width:100%;height:57px;background:var(--green);color:var(--white);font-size:19px;padding:18px 22px}
.service-card.open .overlay{position:absolute;inset:0;background:rgba(125,194,67,.9);color:var(--white);padding:100px 26px 0}
.overlay h4{font-size:18px;font-weight:400;padding-bottom:12px;border-bottom:1px solid rgba(255,255,255,.5);width:60%}
.overlay p{font-size:12px;line-height:1.5;margin-top:14px}
.overlay .btn{margin-top:22px;width:112px;height:40px;border:2px solid var(--white);color:var(--white)}

/* About feature */
.feature{position:absolute;left:0;top:1115px;width:1200px;height:397px}
.feature-photo{left:0;top:0;width:600px;height:397px;background:linear-gradient(180deg,#6e8bab 0%,#b9c5cf 45%,#e8ecef 62%,#2f7fb5 80%,#1b5c8a 100%)}
.play-btn{position:absolute;left:278px;top:176px}
.feature-body{position:absolute;left:600px;top:0;width:600px;height:397px;background:var(--dark);color:var(--white);padding:42px 32px 0 33px}
.feature-body h2{font-size:24px;font-weight:700;line-height:1.3;width:420px}
.feature-body p{font-size:13px;line-height:1.55;margin-top:18px;color:#e2e2e2;width:440px}
.feature-body .btn{margin-top:46px;width:128px;height:42px;border:1px solid var(--green);color:var(--white)}

/* Gallery */
.gallery-title{position:absolute;left:180px;top:1612px;font-size:23px;font-weight:700}
.gallery-title em{font-style:normal;color:var(--green)}
.gallery-title::after{content:"";display:block;width:64px;height:2px;background:var(--line);margin-top:12px}
.gallery-filters{position:absolute;left:180px;top:1672px;font-size:11px;color:#555;display:flex;gap:8px}
.gallery-filters .active{color:var(--green)}
.gallery-item{position:absolute;overflow:hidden}
.gallery-overlay{position:absolute;left:12px;top:12px;right:12px;bottom:12px;background:rgba(125,194,67,.92);color:var(--white);text-align:center;padding-top:40px}
.gallery-overlay h4{font-size:15px;font-weight:400}
.gallery-overlay p{font-size:12px;margin-top:10px;line-height:1.4}
.gallery-overlay .zoom{display:inline-block;margin-top:18px;width:22px;height:22px;background:var(--dark)}
.view-all{position:absolute;left:689px;top:2263px;width:126px;height:38px;border:2px solid #5e9c2c}

/* Testimonials */
.client-avatars{position:absolute;left:415px;top:2462px;width:370px;height:80px}
.avatar{position:absolute;border-radius:50%}
.client-quote{position:absolute;left:240px;top:2550px;width:720px;text-align:center;font-size:14px;line-height:1.5;color:var(--grey-text)}
.client-icon{position:absolute;left:584px;top:2642px}
.client-name{position:absolute;left:0;top:2682px;width:1200px;text-align:center;font-size:14px;font-weight:700}

/* Quote & contact */
.contact-band{position:absolute;left:0;top:2760px;width:1200px;height:308px;background:var(--light-grey)}
.quote-panel{position:absolute;left:155px;top:2824px;width:509px;height:490px;background:linear-gradient(160deg,#5b5b5b,#3e3e3e)}
.quote-strip{position:absolute;left:155px;top:2934px;width:24px;height:330px;background:var(--green)}
.panel-title{font-size:23px;font-weight:700;color:var(--white)}
.panel-title::after{content:"";display:block;width:100%;height:1px;background:rgba(255,255,255,.45);margin-top:14px}
.quote-form{position:absolute;left:232px;top:2882px;width:380px}
.field{height:30px;background:var(--white);margin-top:12px;font-size:11px;color:#888;padding:9px 12px;display:flex;align-items:center;gap:6px}
.field.message{height:96px;align-items:flex-start}
.send-btn{position:absolute;left:552px;top:3174px;width:32px;height:32px;border-radius:50%;background:var(--green);display:flex;align-items:center;justify-content:center}
.contact-panel{position:absolute;left:664px;top:2824px;width:378px;height:490px;background:var(--green);color:var(--white);padding:58px 26px 0 46px}
.contact-panel .panel-title{width:280px}
.contact-block{font-size:13px;line-height:1.4;margin-top:22px}
.contact-block .big{font-size:20px;letter-spacing:1px}
.contact-block a{color:var(--white)}
.socials{display:flex;gap:14px;margin-top:12px}
.socials span{width:32px;height:32px;border-radius:50%;border:1px solid var(--white)}
.socials span.on{background:var(--white)}

/* Footer */
.site-footer{position:absolute;left:208px;top:3358px;font-size:12px;color:#555}
.site-footer em{font-style:normal;color:var(--green)}
.to-top{position:absolute;left:976px;top:3356px}
</style>
</head>
<body>

<header class="site-header">
  <div class="brand"><span class="brand-mark"></span><span class="brand-name">Keel Harbor</span></div>
  <nav class="main-nav">
    <a class="active">Home</a><a>About Us</a><a>Services</a><a>Gallery</a><a>Testimonials</a><a>Contact Us</a>
  </nav>
  <div class="header-phone">
    <svg width="14" height="14" viewBox="0 0 24 24"><path d="M6.6 10.8a15 15 0 0 0 6.6 6.6l2.2-2.2a1 1 0 0 1 1-.25 11.4 11.4 0 0 0 3.6.57 1 1 0 0 1 1 1V20a1 1 0 0 1-1 1A17 17 0 0 1 3 4a1 1 0 0 1 1-1h3.5a1 1 0 0 1 1 1c0 1.25.2 2.45.57 3.57a1 1 0 0 1-.25 1z" fill="#222"/></svg>
    555.014.2280
  </div>
  <a class="btn btn-green header-quote">Get a Quote</a>
</header>

<section class="hero">
  <div class="photo hero-photo" role="img" aria-label="Bright open-plan living room with timber floors, sliding glass doors and a pool view"></div>
  <span class="hero-arrow prev"><svg width="8" height="12"><path d="M7 1 2 6l5 5" stroke="#fff" stroke-width="2" fill="none"/></svg></span>
  <span class="hero-arrow next"><svg width="8" height="12"><path d="M1 1l5 5-5 5" stroke="#fff" stroke-width="2" fill="none"/></svg></span>
  <div class="hero-badge">
    <div class="hero-badge-top">We Provide</div>
    <div class="hero-badge-bottom">➜ Get a Quote</div>
  </div>
  <div class="hero-ribbon">
    <div class="line1">Residential, Commercial, Architectural</div>
    <div class="line2">— ALUMINIUM WINDOWS &amp; DOORS —</div>
  </div>
</section>

<section class="support-bar">
  <svg class="support-icon" width="36" height="36" viewBox="0 0 36 36" fill="none" stroke="#7dc243" stroke-width="2.4"><circle cx="18" cy="15" r="7"/><path d="M6 16a12 12 0 0 1 24 0M6 16v5M30 16v5M6 33c2-6 7-8 12-8s10 2 12 8"/></svg>
  <div class="support-text">
    <h3>24/7 Customer Service &amp; Support</h3>
    <p>There are many variations of passages available majority have suffered</p>
  </div>
  <svg class="support-chev" width="16" height="24"><path d="M2 2l11 10L2 22" stroke="#7dc243" stroke-width="2" fill="none"/></svg>
  <a class="btn btn-green support-contact">Contact Us</a>
  <a class="btn support-free">Get a Free Quote</a>
</section>

<h2 class="section-title" style="top:656px">Our <em>Services</em></h2>

<article class="service-card" style="left:155px">
  <div class="photo" role="img" aria-label="Residential interior with curved floor-to-ceiling glazing overlooking the sea" style="background:linear-gradient(180deg,#9fb8c9,#c28c5a 70%,#8a4e2a)"></div>
  <div class="service-label">Residential</div>
</article>
<article class="service-card open" style="left:461px">
  <div class="photo" role="img" aria-label="Commercial interior with timber ceiling and glass walls" style="background:linear-gradient(180deg,#a57b52,#dcd6cc)"></div>
  <div class="overlay">
    <h4>Commerial</h4>
    <p>There are many variations of passages of Lorem Ipsum available, but the majority have suffered alteration in some form, by injected humour, or randomised...</p>
    <a class="btn">Read More</a>
  </div>
</article>
<article class="service-card" style="left:764px">
  <div class="photo" role="img" aria-label="Architectural home with large sliding glass doors to a patio" style="background:linear-gradient(180deg,#c8ccd0,#6a6e72 55%,#3d4043)"></div>
  <div class="service-label">Architectural</div>
</article>

<section class="feature">
  <div class="photo feature-photo" role="img" aria-label="Modern white house with wide windows beside a blue swimming pool"></div>
  <svg class="play-btn" width="44" height="44" viewBox="0 0 44 44"><circle cx="22" cy="22" r="20" fill="rgba(0,0,0,.2)" stroke="#fff" stroke-width="2"/><path d="M18 14l12 8-12 8z" fill="#fff"/></svg>
  <div class="feature-body">
    <h2>Contrary to popular belief, Lorem Latin literature</h2>
    <p>There are many variations of passages of Lorem Ipsum available, but the majority have suffered alteration in some form, by injected humour, or randomised words.</p>
    <p>If you are going to use a passage of Lorem Ipsum, you need to be sure there isn't anything embarrassing hidden in the middle of text. All the Lorem Ipsum generators on the Internet tend to...</p>
    <a class="btn">About Us</a>
  </div>
</section>

<h2 class="gallery-title">Photo <em>Gallery</em></h2>
<div class="gallery-filters"><span class="active">All</span>|<span>Residential</span>|<span>Commercial</span>|<span>Architectural</span></div>

<div class="gallery-item" style="left:155px;top:1729px;width:281px;height:310px" role="img" aria-label="Timber-clad home with black-framed sliding doors onto a deck"><div class="photo" style="inset:0;background:linear-gradient(180deg,#b89a74,#3a3a38 45%,#9c9891)"></div></div>
<div class="gallery-item" style="left:155px;top:2067px;width:281px;height:262px" role="img" aria-label="Glass sliding doors opening to a garden"><div class="photo" style="inset:0;background:linear-gradient(135deg,#8da39a,#dfe5e3 50%,#6f8479)"></div></div>
<div class="gallery-item" style="left:461px;top:1576px;width:278px;height:199px" role="img" aria-label="White modern building facade with glazing against blue sky"><div class="photo" style="inset:0;background:linear-gradient(135deg,#2f6fb8,#e7eaee 55%,#9aa4ad)"></div></div>
<div class="gallery-item" style="left:461px;top:1802px;width:278px;height:196px">
  <div class="photo" role="img" aria-label="Commercial glazed building" style="inset:0;background:linear-gradient(180deg,#8aa6bd,#6e7f8c)"></div>
  <div class="gallery-overlay"><h4>— Commerial —</h4><p>Contrary to popular belief,<br>Lorem Ipsum is...</p><span class="zoom"></span></div>
</div>
<div class="gallery-item" style="left:461px;top:2025px;width:278px;height:199px" role="img" aria-label="Living area with timber floor and wide glazed doors"><div class="photo" style="inset:0;background:linear-gradient(180deg,#d8d2c8,#9a6a42)"></div></div>
<div class="gallery-item" style="left:764px;top:1576px;width:278px;height:361px" role="img" aria-label="Tall timber house with large gable windows and a deck"><div class="photo" style="inset:0;background:linear-gradient(180deg,#c6d4e0,#7d6148 55%,#5a4636)"></div></div>
<div class="gallery-item" style="left:764px;top:1962px;width:278px;height:262px" role="img" aria-label="Glass curtain-wall office building"><div class="photo" style="inset:0;background:linear-gradient(160deg,#3a6ea8,#9cc0dc 50%,#4c5a66)"></div></div>
<a class="btn btn-green view-all">View All Work</a>

<h2 class="section-title" style="top:2384px">What Our <em>Clients Say</em></h2>
<div class="client-avatars">
  <svg class="abs" style="left:0;top:30px" width="12" height="22"><path d="M10 1 2 11l8 10" stroke="#bbb" stroke-width="2" fill="none"/></svg>
  <div class="avatar" role="img" aria-label="Client portrait" style="left:65px;top:20px;width:52px;height:52px;background:#d8c9b8;opacity:.7"></div>
  <div class="avatar" role="img" aria-label="Client portrait" style="left:145px;top:10px;width:78px;height:78px;background:#8e8a86;border:3px solid #eee"></div>
  <div class="avatar" role="img" aria-label="Client portrait" style="left:250px;top:20px;width:52px;height:52px;background:#d6c3b2;opacity:.7"></div>
  <svg class="abs" style="left:350px;top:30px" width="12" height="22"><path d="M2 1l8 10-8 10" stroke="#7dc243" stroke-width="2" fill="none"/></svg>
</div>
<p class="client-quote">" There are many variations of passages of Lorem Ipsum available, but the majority have suffered alteration in some form, by injected humour, or randomised words which don't look even slightly believable. If you are going...</p>
<svg class="client-icon" width="32" height="32" viewBox="0 0 32 32" fill="none" stroke="#7dc243" stroke-width="2.4"><path d="M6 5h20a2 2 0 0 1 2 2v13a2 2 0 0 1-2 2H14l-7 6v-6H6a2 2 0 0 1-2-2V7a2 2 0 0 1 2-2z"/><path d="M11 13h2M16 13h2M21 13h0"/></svg>
<div class="client-name">Dorian Pell</div>

<div class="contact-band"></div>
<div class="quote-panel"></div>
<div class="quote-strip"></div>
<form class="quote-form">
  <h3 class="panel-title">Get a Free Quote</h3>
  <div class="field" style="margin-top:30px">Your Name</div>
  <div class="field">Enter your Email</div>
  <div class="field">Phone</div>
  <div class="field"><svg width="10" height="10" viewBox="0 0 10 10"><circle cx="5" cy="3" r="2.4" fill="#777"/><path d="M0 10a5 4 0 0 1 10 0z" fill="#777"/></svg>Upload Your File</div>
  <div class="field message">Type your Message</div>
</form>
<span class="send-btn"><svg width="14" height="14" viewBox="0 0 14 14"><path d="M1 7 13 1 9 13 7 8z" fill="#fff"/></svg></span>

<aside class="contact-panel">
  <h3 class="panel-title">Contact Us</h3>
  <div class="contact-block">Keel Harbor:<br>418 Tidewater Row,<br>Port Lennox, KH 20914</div>
  <div class="contact-block">Phone:<br><span class="big">555 - 014 - 2280</span></div>
  <div class="contact-block">Email:<br><a>info@keelharbor.example</a></div>
  <div class="contact-block">Follow Us:
    <div class="socials"><span class="on"></span><span></span><span></span><span></span></div>
  </div>
</aside>

<footer class="site-footer">2017 © <em>Keel Harbor</em>. All rights reserved.</footer>
<svg class="to-top" width="16" height="18"><path d="M8 16V3M2 9l6-6 6 6" stroke="#7dc243" stroke-width="2.4" fill="none"/></svg>

</body>
</html>
```